今回のチラシは当社が年4回発行している会報誌に同梱し、DMで直接お客様へ届けるものになります。
対象は庭付一戸建てに住まわれているお客様がほとんどです。なので、セールスワード(安い、お得、今だけ、限定、キャンペーンなど)をちりばめたようなギラギラしたチラシではなく、当社がお客様のお悩みから解放します的な心情に訴えるチラシにしたいです。
お客様のお困りの原因としては、お勤めでなかなか草むしりする時間が取れない、少し前までは自分でやっていたが年で体力的に難しくなった、奥様がマメに手入れしていたが他界してしまい手つかず状態、親が他界して家を相続したが自分は庭に興味なし。お隣さんから苦情が来てしまう。などなど様々です。
庭木が無くても雑草で困っている方にも、気兼ねなく当社にご依頼してもらえるようなイメージのチラシにしたいです。

トップページ
https://www.574k.co.jp/
除草
https://www.574k.co.jp/weeding/
砂利敷き(防草シート含む)
https://www.574k.co.jp/gravel/
表面:キャッチコピー、キャッチコピーに合う写真などの組合せ※情報はこの2つにしてシンプルに。
裏面:社名、支払い方法、フリーダイヤル、URL、QRコードなど ※添付資料参照
A4
両面
シンプル 複雑
単色 カラフル
暗い 明るい
日常 高級
遊び心 厳粛
未来的 伝統的
女性的 男性的
黄・オレンジ系、緑系、茶系
• イラストレーター形式 (.ai)
印刷用のPDFも納品ください。

情報量を少なくしシンプルにまとまっている。
お客様のお困りごとを端的に示していて伝わりやすい。
裏面にある商品説明の記載内容は必要十分の情報量で綺麗に整理されていて読みやすい。

皆様、この度は弊社のチラシ作成に応募いただき誠にありがとうございました。
社内で投票を行いましたが、どれかに集中することなく票がばらける程どれも良い感じだったと思います。
またチラシ作成やその他で募集させていただく際は是非ご応募ください。

```html
<!DOCTYPE html>
<html lang="ja">
<head>
<meta charset="utf-8">
<title>草刈り・草むしり・砂利敷き | 植木屋新風</title>
<link rel="stylesheet" href="https://fonts.googleapis.com/css2?family=Noto+Sans+JP:wght@500;700;900&display=swap">
<style>
  :root {
    --green-top: #7ccd3f;
    --green-mid: #4fb338;
    --green-base: #3da434;
    --green-deep: #2a8a2c;
    --grass-light: #9ad658;
    --grass-dark: #2f7f26;
    --wave-light: #b7e27a;
    --white: #ffffff;
    --accent-yellow: #f7ea1c;
  }
  html, body {
    margin: 0;
    padding: 0;
    overflow: hidden;
  }
  body {
    width: 849px;
    height: 1200px;
    font-family: "Noto Sans JP", sans-serif;
  }
  .flyer {
    position: relative;
    width: 849px;
    height: 1200px;
    overflow: hidden;
    background: linear-gradient(180deg, var(--green-top) 0%, var(--green-mid) 45%, var(--green-base) 100%);
    color: var(--white);
  }
  .flyer__scenery {
    position: absolute;
    inset: 0;
    width: 849px;
    height: 1200px;
  }
  .headline {
    position: absolute;
    margin: 0;
    writing-mode: vertical-rl;
    font-weight: 900;
    letter-spacing: 0.02em;
    line-height: 1;
    text-shadow: 0 2px 8px rgba(20, 70, 20, 0.25);
  }
  .headline--mowing {
    left: 418px;
    top: 322px;
    font-size: 100px;
  }
  .headline--weeding {
    left: 253px;
    top: 210px;
    font-size: 100px;
  }
  .headline--gravel {
    left: 136px;
    top: 440px;
    font-size: 56px;
  }
  .message {
    position: absolute;
    left: 516px;
    top: 760px;
    margin: 0;
    font-size: 30px;
    font-weight: 700;
    line-height: 42px;
    letter-spacing: 0.12em;
  }
  .message__highlight {
    color: var(--accent-yellow);
  }
  .brand {
    position: absolute;
    left: 0;
    right: 0;
    top: 1018px;
    text-align: center;
  }
  .brand__roman {
    display: flex;
    align-items: center;
    justify-content: center;
    gap: 12px;
    font-size: 22px;
    font-weight: 700;
    letter-spacing: 0.08em;
  }
  .brand__dot {
    width: 14px;
    height: 14px;
    border-radius: 50%;
    background: var(--white);
  }
  .brand__name {
    margin-top: 6px;
    font-size: 54px;
    font-weight: 700;
    letter-spacing: 0.04em;
    line-height: 1.2;
  }
</style>
</head>
<body>
  <main class="flyer">
    <svg class="flyer__scenery" viewBox="0 0 849 1200" aria-hidden="false">
      <defs>
        <linearGradient id="grassFill" x1="0" y1="0" x2="0" y2="1">
          <stop offset="0" stop-color="var(--grass-light)" stop-opacity="0"/>
          <stop offset="0.25" stop-color="var(--grass-light)" stop-opacity="0.7"/>
          <stop offset="0.7" stop-color="var(--grass-dark)"/>
          <stop offset="1" stop-color="var(--green-deep)"/>
        </linearGradient>
        <linearGradient id="waveFill" x1="1" y1="0" x2="0" y2="1">
          <stop offset="0" stop-color="var(--wave-light)"/>
          <stop offset="1" stop-color="var(--green-mid)"/>
        </linearGradient>
      </defs>
      <path class="scenery__grass" role="img" aria-label="青々と茂る雑草と野草の写真"
            d="M0 110 L849 110 L849 560 C620 620 420 760 0 790 Z"
            fill="url(#grassFill)"/>
      <path class="scenery__wave"
            d="M0 770 C380 760 560 610 849 500 L849 600 C560 680 380 820 0 850 Z"
            fill="url(#waveFill)" opacity="0.85"/>
      <path class="scenery__ground"
            d="M0 850 C380 820 560 680 849 600 L849 1200 L0 1200 Z"
            fill="var(--green-base)"/>
    </svg>

    <h1 class="headline headline--mowing">草刈り</h1>
    <p class="headline headline--weeding">草むしり</p>
    <p class="headline headline--gravel">砂利敷き</p>

    <p class="message">
      お庭の<br>
      <span class="message__highlight">ちょっとした</span><br>
      <span class="message__highlight">お手入れ</span><br>
      承ります。
    </p>

    <footer class="brand">
      <div class="brand__roman"><span>UEKIYA</span><span class="brand__dot"></span><span>SHINPU</span></div>
      <div class="brand__name">植木屋新風</div>
    </footer>
  </main>
</body>
</html>
```